Cedar Hollow Candle Banner Ad for Upcoming holidays

We would like for you to design an ad for Memorial day and Father's Day. For Memorial Day the sale will be 25% OFF select candles and free shipping when you order $50 or more.
For father's day the deal will be get 30% off all candles and free shipping when you order $75 or more.
Please note: These banners will be on our website, they do not require our logo.Banner size: 314 height x 783 width

Industry/Entity Type

Shipping

Requirements
Must have
• Banner size: 314 height x 783 width
Nice to have
• Picture of our starlit candle
Should not have
• Logo

```html
<!DOCTYPE html>
<html lang="en">
<head>
<meta charset="utf-8">
<title>Cedar Hollow Candle – Holiday Banners</title>
<link href="https://fonts.googleapis.com/css2?family=Playfair+Display:wght@400;500&family=Marcellus&family=Lato:wght@400&display=swap" rel="stylesheet">
<style>
  :root{
    --page:#ecebe9;
    --ink-dark:#1f1c1d;
    --ink-dark-2:#2b2628;
    --white:#ffffff;
    --gold:#c99a5b;
    --gold-deep:#b8862f;
    --gold-bright:#d9a93a;
    --warm-1:#c98d4e;
    --warm-2:#e2b47a;
    --warm-3:#8a5a34;
  }
  *{box-sizing:border-box;margin:0;padding:0}
  html,body{width:1200px;height:1000px;overflow:hidden;background:var(--page)}
  .banner{position:absolute;left:215px;width:782px;height:314px;overflow:hidden;color:var(--white)}
  .banner--fathers{top:167px}
  .banner--memorial{top:549px;background:linear-gradient(90deg,var(--ink-dark-2),#231f21 70%,#2a2527)}
  .art{position:absolute}
  .fathers__photo{inset:0;background:linear-gradient(120deg,var(--warm-2) 0%,var(--warm-1) 40%,var(--warm-3) 65%,#d9a46a 85%,#f1dcc0 100%)}
  .fathers__panel{position:absolute;inset:0}
  .fathers__title{position:absolute;left:14px;top:12px;font-family:"Playfair Display",serif;font-weight:400;line-height:.86;letter-spacing:-1px}
  .fathers__title .line1{display:block;font-size:46px;padding-left:36px}
  .fathers__title .line2{display:block;font-size:46px}
  .fathers__title .accent{color:var(--gold)}
  .discount{position:absolute;font-family:"Playfair Display",serif;color:var(--gold);display:flex;align-items:flex-start;line-height:1}
  .discount__num{font-weight:500}
  .discount__tail{display:flex;flex-direction:column;align-items:center}
  .fathers__discount{left:27px;top:134px}
  .fathers__discount .discount__num{font-size:58px}
  .fathers__discount .discount__pct{font-size:24px}
  .fathers__discount .discount__off{font-size:40px;margin-top:-8px}
  .cta{position:absolute;left:53px;top:220px;width:84px;height:24px;border:1px solid var(--white);font-family:"Lato",sans-serif;font-size:10px;display:flex;align-items:center;justify-content:center;color:var(--white);text-decoration:none}
  .shipping{position:absolute;font-family:"Playfair Display",serif;line-height:1.3}
  .shipping__title{font-size:16px}
  .shipping__note{font-size:10.5px}
  .fathers__shipping{left:14px;top:272px}
  .memorial__flag{left:0;top:0;width:300px;height:314px;background:linear-gradient(90deg,#6d2030 0%,#3e3b63 35%,#34304c 60%,rgba(43,38,40,0) 100%)}
  .memorial__candles{left:225px;top:105px;width:240px;height:190px;border-radius:8px;background:linear-gradient(90deg,#6cb6c6 0%,#dfe3e4 50%,#ede4d8 75%,#c7c9cb 100%)}
  .memorial__title{position:absolute;left:306px;top:34px;font-family:"Marcellus",serif;font-size:29px;letter-spacing:.17em;white-space:nowrap}
  .memorial__discount{left:518px;top:96px}
  .memorial__discount .discount__num{font-size:96px;color:var(--gold-bright)}
  .memorial__discount .discount__pct{font-size:36px;color:var(--gold-bright)}
  .memorial__discount .discount__off{font-size:56px;margin-top:-10px;color:var(--gold-deep)}
  .memorial__shipping{right:28px;top:256px;text-align:right}
</style>
</head>
<body>
  <section class="banner banner--fathers">
    <div class="art fathers__photo" role="img" aria-label="Study with ornate desk, open book, leather chair and Cedar Hollow Candle starlit candles"></div>
    <svg class="fathers__panel" viewBox="0 0 782 314" width="782" height="314" aria-hidden="true">
      <defs>
        <linearGradient id="panelShade" x1="0" y1="0" x2="1" y2="1">
          <stop offset="0" stop-color="#2a2627"/>
          <stop offset="1" stop-color="#181617"/>
        </linearGradient>
      </defs>
      <polygon points="0,0 312,0 183,314 0,314" fill="url(#panelShade)"/>
    </svg>
    <h2 class="fathers__title"><span class="line1">Father’s</span><span class="line2">DayGift<span class="accent">Sale</span></span></h2>
    <div class="discount fathers__discount"><span class="discount__num">25</span><span class="discount__tail"><span class="discount__pct">%</span><span class="discount__off">off</span></span></div>
    <a class="cta" href="#">SHOP NOW!</a>
    <div class="shipping fathers__shipping"><div class="shipping__title">Free Shipping</div><div class="shipping__note">*when you order $75 or more.</div></div>
  </section>

  <section class="banner banner--memorial">
    <div class="art memorial__flag" role="img" aria-label="Draped American flag"></div>
    <div class="art memorial__candles" role="img" aria-label="Two lit three-wick Cedar Hollow Candle jar candles with lids"></div>
    <h2 class="memorial__title">MEMORIAL DAY SALE</h2>
    <div class="discount memorial__discount"><span class="discount__num">25</span><span class="discount__tail"><span class="discount__pct">%</span><span class="discount__off">Off</span></span></div>
    <div class="shipping memorial__shipping"><div class="shipping__title">Free Shipping</div><div class="shipping__note">*when you order $50 or more.</div></div>
  </section>
</body>
</html>
```